Aisle Bloom Bridal Show Flyer

I need designed a reusable flyer that is more eye catching than my current flyer. I would also need separate layers as the details change from show to show. I attached the flyer I currently use.

Industry/Entity Type

Wedding

```html
<!DOCTYPE html>
<html lang="en">
<head>
<meta charset="utf-8">
<title>Aisle Bloom Bridal Show Flyer</title>
<link rel="stylesheet" href="https://fonts.googleapis.com/css2?family=Great+Vibes&family=Roboto:wght@400;500&family=Roboto+Condensed:wght@400;700&display=swap">
<style>
  :root {
    --stage: #ebe6e0;
    --paper: #ffffff;
    --paper-shade: #eef0ee;
    --green: #1f7a25;
    --green-dark: #2a7a2a;
    --navy: #24358a;
    --ink: #333333;
    --sky: #4eaaea;
    --sky-light: #bcdcf4;
    --photo-a: #2f6a2a;
    --photo-b: #8cbf6c;
  }
  * { box-sizing: border-box; margin: 0; padding: 0; }
  html, body { width: 1200px; height: 1000px; overflow: hidden; background: var(--stage); }
  .flyer {
    position: absolute; left: 253px; top: 48px; width: 694px; height: 900px;
    background: linear-gradient(100deg, var(--paper-shade) 0%, var(--paper) 45%);
    overflow: hidden; font-family: "Roboto", Arial, sans-serif; color: var(--ink);
  }
  .flyer-shapes { position: absolute; inset: 0; }
  .abs { position: absolute; }
  .script { font-family: "Great Vibes", cursive; font-weight: 400; }
  .title-bridal { left: 40px; top: 42px; font-size: 92px; color: var(--green); line-height: 1; }
  .title-show { left: 240px; top: 128px; font-size: 92px; color: var(--green); line-height: 1; }
  .casting { left: 0; width: 414px; top: 248px; text-align: center; font-size: 27px; }
  .tagline { left: 0; width: 414px; top: 284px; text-align: center; font-size: 29px; white-space: nowrap; }
  .tagline .script { color: var(--navy); font-size: 46px; }
  .rule { left: 30px; width: 350px; border-top: 1px dotted #b5b5b5; }
  .prize { left: 30px; width: 350px; top: 356px; display: flex; align-items: center; justify-content: center; gap: 12px; }
  .prize-note { font-size: 13.5px; line-height: 1.05; text-align: right; text-transform: uppercase; }
  .prize-amount { font-size: 33px; font-weight: 500; color: var(--green); }
  .details { left: 0; width: 414px; top: 412px; text-align: center; font-family: "Roboto Condensed", Arial, sans-serif; }
  .details .when { font-size: 18px; }
  .details .when b { color: var(--green); font-weight: 700; }
  .details .venue { font-size: 22px; font-weight: 700; color: var(--navy); margin-top: 4px; }
  .details .address { font-size: 17px; margin-top: 4px; }
  .coupon {
    left: 51px; top: 508px; width: 341px; height: 38px; background: var(--green-dark);
    border: 2px dashed #8fc48a; color: #fff; display: flex; align-items: center; justify-content: center;
    font-family: "Roboto Condensed", Arial, sans-serif; font-size: 16px; gap: 6px;
  }
  .coupon b { font-size: 19px; }
  .cruise-photo {
    left: 47px; top: 566px; width: 202px; height: 92px; border-radius: 8px;
    background: linear-gradient(180deg, #8fd0ee 0%, #4aaed8 55%, #1c86b8 100%);
  }
  .radio-partner {
    left: 264px; top: 566px; width: 144px; height: 92px; border: 4px solid var(--navy);
    border-radius: 12px; background: #fff; display: flex; align-items: center; justify-content: center;
    font-size: 24px; font-weight: 500; color: var(--navy);
  }
  .giveaway { left: 40px; width: 244px; top: 670px; text-align: center; color: var(--green); font-size: 34px; line-height: 1.2; }
  .brand { left: 32px; top: 816px; font-size: 40px; color: #fff; font-weight: 400; letter-spacing: 0.5px; }
  .divider { left: 417px; top: 724px; height: 152px; border-left: 1.5px solid #fff; }
  .info { left: 432px; top: 714px; color: #fff; font-family: "Roboto Condensed", Arial, sans-serif; }
  .info .label { font-size: 23px; }
  .info .url { font-size: 30px; font-weight: 700; line-height: 1.1; }
  .info .label-sm { font-size: 19px; margin-top: 14px; }
  .info .sponsor { font-size: 29px; line-height: 1.08; }
</style>
</head>
<body>
<main class="flyer">
  <svg class="flyer-shapes" width="694" height="900" viewBox="0 0 694 900">
    <defs>
      <linearGradient id="photoTone" x1="0" y1="0" x2="1" y2="1">
        <stop offset="0" stop-color="var(--photo-a)"/>
        <stop offset="0.6" stop-color="#4f8a3e"/>
        <stop offset="1" stop-color="var(--photo-b)"/>
      </linearGradient>
    </defs>
    <path role="img" aria-label="Photo of a smiling bride in a strapless gown with a birdcage veil, green foliage behind"
          d="M694 37 L570 37 C460 70 402 240 402 380 C402 520 470 640 580 710 L694 710 Z"
          fill="url(#photoTone)" stroke="#fff" stroke-width="6"/>
    <path d="M0 742 C150 712 280 668 500 652 C600 646 660 658 694 676 L694 900 L0 900 Z" fill="var(--sky-light)"/>
    <path d="M0 768 C150 738 280 692 500 676 C600 670 660 682 694 700 L694 900 L0 900 Z" fill="var(--sky)"/>
  </svg>

  <h1>
    <span class="abs script title-bridal">Bridal</span>
    <span class="abs script title-show">Show</span>
  </h1>
  <p class="abs casting">Open Casting Call</p>
  <p class="abs tagline">Say <span class="script">Yes</span> to the <span class="script">Gown</span></p>

  <div class="abs rule" style="top:349px"></div>
  <div class="abs prize">
    <p class="prize-note">The first 50 brides will<br>get a chance to win</p>
    <p class="prize-amount">$25,000</p>
  </div>
  <div class="abs rule" style="top:400px"></div>

  <div class="abs details">
    <p class="when">Tuesday <b>•</b> September 16th <b>•</b> 6:00-9:00 PM</p>
    <p class="venue">The Harbor Room at Marcello's</p>
    <p class="address">1190 Shore Lane, Millbrook, CT</p>
  </div>

  <p class="abs coupon"><b>$3</b> off admission by using coupon code NP3</p>

  <div class="abs cruise-photo" role="img" aria-label="Photo of a white cruise ship on turquoise water"></div>
  <div class="abs radio-partner">Bright FM</div>

  <p class="abs script giveaway">Honeymoon<br>Cruise Giveaway</p>

  <p class="abs brand">Aisle Bloom</p>
  <div class="abs divider"></div>
  <div class="abs info">
    <p class="label">Get Tickets at</p>
    <p class="url">aislebloom.com</p>
    <p class="label-sm">Sponsored by</p>
    <p class="sponsor">Rhythm &amp; Vows<br>Entertainment</p>
  </div>
</main>
</body>
</html>
```